Covert current Brochures from PDF to PDF editable, No need to change the format

We have 3 brochures that need to be updated in the template to make the content editable. No need to change the format.

```html
<!DOCTYPE html>
<html lang="en">
<head>
<meta charset="utf-8">
<title>Hearth Lane Care Services – Breakdown of Service Fees, Level 1</title>
<link rel="stylesheet" href="https://fonts.googleapis.com/css2?family=Barlow:ital,wght@0,400;0,500;0,600;0,700;1,400;1,500&family=Barlow+Condensed:wght@700&display=swap">
<style>
  :root {
    --navy: #35308f;
    --red: #cc3b2a;
    --periwinkle: #7b8bcb;
    --sky: #8fd3ea;
    --cell-navy: #1f5db0;
    --cell-red: #7a6169;
    --cell-periwinkle: #4aa5d9;
    --page: #eff0f4;
    --grey-text: #5a5a62;
    --white: #ffffff;
  }
  * { box-sizing: border-box; margin: 0; padding: 0; }
  html, body { width: 894px; height: 1200px; overflow: hidden; }
  body {
    position: relative;
    font-family: "Barlow", Arial, sans-serif;
    background: linear-gradient(160deg, #f6f7f9 0%, var(--page) 60%, #e9eaef 100%);
  }
  .hero-photo {
    position: absolute; left: 0; top: 0; width: 894px; height: 650px;
    background:
      radial-gradient(ellipse at 25% 40%, #dfe6ee 0%, rgba(223,230,238,0) 55%),
      radial-gradient(ellipse at 75% 55%, #a9c9e4 0%, rgba(169,201,228,0) 50%),
      linear-gradient(180deg, #e6e9ee 0%, #eef0f4 70%, rgba(239,240,244,0) 100%);
  }
  .brand-mark {
    position: absolute; left: 0; width: 894px; top: 150px;
    text-align: center; color: var(--navy);
    font-weight: 700; font-size: 34px; letter-spacing: 0.5px; line-height: 1;
  }
  .brand-mark .dot {
    display: inline-block; width: 16px; height: 16px; border-radius: 50%;
    background: var(--navy); margin-right: 10px; vertical-align: 3px;
  }
  .title {
    position: absolute; left: 0; width: 894px; top: 420px;
    text-align: center; color: var(--red);
    font-family: "Barlow Condensed", "Arial Narrow", sans-serif;
    font-weight: 700; font-size: 58px; line-height: 64px; letter-spacing: 1px;
  }
  .level-pill {
    position: absolute; left: 324px; top: 559px; width: 244px; height: 59px;
    border-radius: 20px; background: var(--navy); color: var(--white);
    font-weight: 700; font-size: 30px; text-align: center; line-height: 59px; letter-spacing: 1px;
  }
  .fee-table { position: absolute; left: 0; top: 0; }
  .col-band {
    position: absolute; top: 651px; height: 258px; width: 157px;
    background: var(--sky); border-radius: 10px;
  }
  .col-band.daily { left: 385px; }
  .col-band.yearly { left: 560px; }
  .col-head {
    position: absolute; top: 670px; width: 157px; text-align: center;
    color: var(--white); font-weight: 600; font-size: 20px; letter-spacing: 0.5px;
  }
  .row-band {
    position: absolute; left: 149px; width: 596px; height: 54px;
    color: var(--white); font-weight: 700; font-size: 21px; line-height: 54px;
    padding-left: 22px;
  }
  .row-band.subsidy { top: 715px; background: var(--navy); }
  .row-band.fees { top: 774px; background: var(--red); }
  .row-band.provisions { top: 843px; background: var(--periwinkle); }
  .cell {
    position: absolute; width: 157px; height: 54px; line-height: 54px;
    text-align: center; color: var(--white); font-weight: 700; font-size: 21px; letter-spacing: 0.5px;
  }
  .cell.daily { left: 385px; }
  .cell.yearly { left: 560px; }
  .cell.subsidy { top: 715px; background: var(--cell-navy); }
  .cell.fees { top: 774px; background: var(--cell-red); }
  .cell.provisions { top: 843px; background: var(--cell-periwinkle); }
  .hours {
    position: absolute; left: 0; width: 894px; top: 926px;
    text-align: center; color: var(--navy); font-weight: 500; font-size: 31px;
  }
  .hours strong {
    color: var(--red); font-family: "Barlow Condensed", "Arial Narrow", sans-serif;
    font-size: 52px; margin-left: 8px; letter-spacing: 1px;
  }
  .hours-note {
    position: absolute; left: 0; width: 894px; top: 997px;
    text-align: center; color: #b02a22; font-style: italic; font-size: 16px; letter-spacing: -0.2px;
  }
  .footnote {
    position: absolute; left: 0; width: 894px; top: 1075px;
    text-align: center; color: var(--grey-text); font-style: italic; font-size: 15px; line-height: 20px;
  }
  .footer {
    position: absolute; left: 0; top: 1142px; width: 894px; height: 58px;
    background: var(--navy); color: var(--white); font-size: 16px; font-weight: 500;
  }
  .contact { position: absolute; top: 0; height: 58px; display: flex; align-items: center; gap: 6px; }
  .contact.phone { left: 89px; letter-spacing: 1px; }
  .contact.email { left: 256px; }
  .contact svg { width: 24px; height: 24px; }
  .footer-brand {
    position: absolute; right: 66px; top: 0; line-height: 58px;
    color: var(--red); font-size: 19px;
  }
</style>
</head>
<body>
  <div class="hero-photo" role="img" aria-label="Photograph of a smiling senior woman with a carer in blue scrubs resting a hand on her shoulder"></div>

  <div class="brand-mark"><span class="dot"></span>HEARTH LANE CARE SERVICES</div>

  <h1 class="title">BREAKDOWN OF<br>SERVICE FEES</h1>
  <div class="level-pill">LEVEL 1</div>

  <div class="fee-table">
    <div class="col-band daily"></div>
    <div class="col-band yearly"></div>
    <div class="col-head" style="left:385px">DAILY</div>
    <div class="col-head" style="left:560px">YEARLY</div>

    <div class="row-band subsidy">Subsidy Received</div>
    <div class="row-band fees">Total Fees (20%)*</div>
    <div class="row-band provisions">Service Provisions</div>

    <div class="cell daily subsidy">$28.14</div>
    <div class="cell yearly subsidy">$10271.10</div>
    <div class="cell daily fees">$5.628</div>
    <div class="cell yearly fees">$2054.22</div>
    <div class="cell daily provisions">$22.512</div>
    <div class="cell yearly provisions">$8216.88</div>
  </div>

  <p class="hours">Hours per fortnight <strong>4.75</strong></p>
  <p class="hours-note">Hours of services provided is affected by requested of allied health, lawn mowing and/or equipment.</p>
  <p class="footnote">*Total fees: see Hearth Lane Care Services Agreement for details. Fees are subject to change<br>and reviewed annually. Clients and/or representatives to be advised of any changes.</p>

  <footer class="footer">
    <div class="contact phone">
      <svg viewBox="0 0 24 24" aria-hidden="true"><circle cx="12" cy="12" r="12" fill="#e8574a"/><path d="M8.2 6.5l2 2.3-1.1 1.6c.8 1.7 2 2.9 3.7 3.7l1.6-1.1 2.3 2-1.2 2c-4.6-.3-8.3-4-8.6-8.6z" fill="#fff"/></svg>
      <span>1800 555 012</span>
    </div>
    <div class="contact email">
      <svg viewBox="0 0 24 24" aria-hidden="true"><circle cx="12" cy="12" r="12" fill="#e8574a"/><rect x="6" y="8" width="12" height="8.5" rx="1" fill="#fff"/><path d="M6.5 8.6l5.5 4 5.5-4" stroke="#e8574a" stroke-width="1.2" fill="none"/></svg>
      <span>hello@hearthlanecare.com.au</span>
    </div>
    <div class="footer-brand">Hearth Lane Care Services</div>
  </footer>
</body>
</html>
```